Business Card Re-Design/Update

We'd like to update out business cards. I've included our current "Style guide" which has the colour scheme of the organisation in it. I've also included the branding files with logos etc in them.

I've also included a copy of one of our existing cards so that you can see how ugly/dated they look. I'd like a fresh modern corporate look.

Target Market(s)

These are for our clients, potential clients, industry contacts - like all business cards

Contact Information for Business Card

Name
Position
Company Address - Level 1, 47 Garnet Lane, Toowong Qld 4066
Direct Phone
mobile
Email
Website -www.korvalnet.com.au
Logo

Colors

Designer to choose colors to be used in the design.

Requirements
Must have
• Main Logo
• Cards will need to be editable to be able to personalize them for each new employee.
Nice to have
• The MapOUT, HandOVER, UpKEEP would be okay to have if they can be sensibly and professionally added to the look without detracting from the main imagery.
• Maybe they could go on the back of the card? will leave this to your creative discretion as to whether/where they fit.
Should not have
• Should not have decorative or script fonts

```html
<!DOCTYPE html>
<html lang="en">
<head>
<meta charset="utf-8">
<title>korvalNET – Business Card Proposal</title>
<link rel="stylesheet" href="https://fonts.googleapis.com/css2?family=Arimo:wght@400;700&family=Bebas+Neue&display=swap">
<style>
  :root {
    --brand-red: #ff0000;
    --ink: #1f1f1f;
    --ink-soft: #555555;
    --paper: #ffffff;
    --band: #a9a9a9;
    --mark: #2b2b2b;
    --handover: #3a9cf2;
    --mapout: #55c900;
    --upkeep: #a21ff0;
  }
  * { box-sizing: border-box; margin: 0; padding: 0; }
  html, body { width: 1200px; height: 1200px; overflow: hidden; background: var(--paper); }
  body { position: relative; font-family: "Arimo", Arial, sans-serif; color: var(--ink); }

  .label {
    position: absolute; left: 230px;
    font-family: "Bebas Neue", "Arial Narrow", sans-serif;
    font-size: 44px; line-height: 1; color: #000;
  }
  .label--front { top: 494px; }
  .label--reverse { top: 1006px; }

  /* Front */
  .card-front {
    position: absolute; left: 230px; top: 80px; width: 696px; height: 387px;
    background: var(--brand-red);
  }
  .card-front .wordmark {
    position: absolute; left: 0; right: 0; top: 200px;
    display: flex; align-items: center; justify-content: center; gap: 22px;
    color: var(--paper); font-size: 86px; font-weight: 400; letter-spacing: -1px;
    transform: translateY(-50%);
  }
  .wordmark__square { width: 60px; height: 60px; background: currentColor; flex: none; }
  .services {
    position: absolute; right: 0; top: 292px; width: 277px; height: 56px;
    background: var(--paper);
    display: flex; align-items: center; justify-content: space-around; padding: 0 8px;
  }
  .service { display: flex; flex-direction: column; align-items: center; gap: 3px;
    font-size: 14px; font-weight: 700; }
  .service__square { width: 14px; height: 14px; background: currentColor; transform: rotate(45deg); }
  .service--handover { color: var(--handover); }
  .service--mapout { color: var(--mapout); }
  .service--upkeep { color: var(--upkeep); }

  /* Reverse */
  .card-back { position: absolute; left: 230px; top: 588px; width: 696px; height: 387px; }
  .crop { position: absolute; width: 43px; height: 43px; border-color: #222; border-style: solid; border-width: 0; }
  .crop--tl { left: 0; top: 0; border-top-width: 1.5px; border-left-width: 1.5px; }
  .crop--tr { right: 0; top: 0; border-top-width: 1.5px; border-right-width: 1.5px; }
  .crop--bl { left: 0; bottom: 0; border-bottom-width: 1.5px; border-left-width: 1.5px; }
  .crop--br { right: 0; bottom: 0; border-bottom-width: 1.5px; border-right-width: 1.5px; }

  .brand-block { position: absolute; left: 22px; top: 50px; width: 310px; text-align: center; }
  .brand-block__square { width: 56px; height: 56px; margin: 0 auto 14px; background: var(--brand-red); transform: rotate(45deg); }
  .brand-block__name { font-size: 47px; font-weight: 400; color: var(--mark); line-height: 1; letter-spacing: -0.5px; }
  .brand-block__web {
    margin-top: 8px; background: var(--brand-red); color: var(--paper);
    font-size: 20px; font-weight: 700; line-height: 27px;
  }
  .address { position: absolute; left: 23px; top: 258px; font-size: 20px; font-weight: 700;
    color: var(--ink-soft); line-height: 29px; }

  .person { position: absolute; left: 393px; top: 74px; }
  .person__name { font-size: 35px; line-height: 1.1; color: var(--ink); }
  .person__role { font-size: 20px; color: var(--brand-red); margin-top: 2px; }

  .contacts { position: absolute; right: 20px; top: 232px; text-align: right; list-style: none; }
  .contacts li { font-size: 24px; line-height: 43px; white-space: nowrap; }
  .contacts .key { color: var(--brand-red); }
  .contacts .sep { display: inline-block; width: 1px; height: 24px; background: var(--brand-red);
    margin: 0 4px 0 3px; vertical-align: -4px; }

  .footer-band {
    position: absolute; left: 0; top: 1086px; width: 1200px; height: 114px;
    background: var(--band); display: flex; align-items: center; padding-left: 56px;
  }
  .footer-band__title { font-family: "Bebas Neue", "Arial Narrow", sans-serif; font-size: 54px; color: var(--paper); }
</style>
</head>
<body>

  <section class="card-front" aria-label="Card front">
    <div class="wordmark"><span class="wordmark__square"></span><span>korvalNET</span></div>
    <div class="services">
      <div class="service service--handover"><span class="service__square"></span>HandOVER</div>
      <div class="service service--mapout"><span class="service__square"></span>MapOUT</div>
      <div class="service service--upkeep"><span class="service__square"></span>UpKEEP</div>
    </div>
  </section>
  <div class="label label--front">Front</div>

  <section class="card-back" aria-label="Card reverse">
    <span class="crop crop--tl"></span><span class="crop crop--tr"></span>
    <span class="crop crop--bl"></span><span class="crop crop--br"></span>

    <div class="brand-block">
      <div class="brand-block__square"></div>
      <div class="brand-block__name">korvalNET</div>
      <div class="brand-block__web">www.korvalnet.com.au</div>
    </div>
    <p class="address">Level 1, 47 Garnet Lane,<br>Toowong Qld 4066</p>

    <div class="person">
      <div class="person__name">Marla Jensen</div>
      <div class="person__role">Executive</div>
    </div>

    <ul class="contacts">
      <li><span class="key">DP</span><span class="sep"></span>(07) 3190 4417</li>
      <li><span class="key">M</span><span class="sep"></span>0412 608 735</li>
      <li><span class="key">M</span><span class="sep"></span>marla.j@korvalnet.com.au</li>
    </ul>
  </section>
  <div class="label label--reverse">Reverse</div>

  <footer class="footer-band">
    <span class="footer-band__title">Business Card Proposal</span>
  </footer>

</body>
</html>
```